Business card design needed

We design, manufacture and install kitchen robes vanity etc.
We have a current card that i want to upload that you can base the design around and make suggestions for other design but we need the logo to be unchanged that i will up load along with our current card.

Industry/Entity Type

Business

Contact Information for Business Card

Tallowind Joinery Works
Dorian Calvestri
47 Quarrington Avenue, Hallsbury S.A 5099
dorian@tallowindjoinery.com.au
Lic. No. Bld 582904 Bld 740251

```html
<!DOCTYPE html>
<html lang="en">
<head>
<meta charset="utf-8">
<title>Tallowind Joinery Works – Business Card</title>
<link rel="stylesheet" href="https://fonts.googleapis.com/css2?family=Open+Sans:wght@400;600&family=Tinos:wght@400;700&family=Gelasio:wght@400;700&display=swap">
<style>
  :root {
    --backdrop: #2a2a2a;
    --card: #fbfbfb;
    --green: #8fa043;
    --green-soft: #9aab4e;
    --grey: #c9c9c9;
    --grey-light: #e2e2e2;
    --ink: #555555;
    --ink-dark: #1c1c1c;
    --black: #111111;
  }
  * { box-sizing: border-box; margin: 0; padding: 0; }
  html, body { width: 1200px; height: 900px; overflow: hidden; }
  body {
    background: var(--backdrop);
    position: relative;
    font-family: "Open Sans", Arial, sans-serif;
  }
  .card {
    position: absolute;
    left: 290px;
    width: 620px;
    height: 355px;
    background: var(--card);
    overflow: hidden;
    box-shadow: 0 10px 30px rgba(0,0,0,.5);
  }
  .card--contact { top: 60px; }
  .card--services { top: 480px; }

  /* contact side */
  .contact__edge { position: absolute; left: 0; top: 0; width: 42px; height: 100%; background: var(--grey-light); }
  .contact__corner { position: absolute; right: 0; top: 0; width: 60px; height: 60px; background: var(--grey-light); }
  .contact__band { position: absolute; right: 0; top: 150px; width: 340px; height: 34px; background: var(--green); }
  .contact__tab { position: absolute; left: 0; top: 232px; width: 80px; height: 22px; background: var(--green); }
  .brand {
    font-family: "Open Sans", Arial, sans-serif;
    font-weight: 600;
    color: var(--green);
    letter-spacing: .5px;
    display: flex;
    align-items: center;
    gap: 10px;
    white-space: nowrap;
  }
  .brand__dot { width: 12px; height: 12px; border-radius: 50%; background: var(--green); flex: none; }
  .contact__brand { position: absolute; right: 70px; top: 62px; font-size: 19px; }
  .contact__name {
    position: absolute; left: 95px; top: 222px;
    font-family: "Tinos", "Times New Roman", serif;
    font-size: 34px; color: var(--ink); font-weight: 400;
  }
  .contact__details {
    position: absolute; left: 95px; top: 268px;
    font-size: 13px; line-height: 22px; color: var(--ink);
  }
  .contact__details span { margin-right: 16px; }

  /* services side */
  .services__shapes { position: absolute; inset: 0; }
  .services__brand {
    position: absolute; left: 140px; right: 20px; top: 102px;
    justify-content: center; font-size: 28px; color: var(--green);
  }
  .services__title {
    position: absolute; left: 160px; top: 188px;
    font-family: "Tinos", "Times New Roman", serif;
    font-weight: 700; font-size: 21px; color: var(--ink-dark);
  }
  .services__list {
    position: absolute; left: 160px; top: 226px;
    list-style: none;
    display: grid;
    grid-template-columns: 130px 130px 220px;
    row-gap: 4px;
    font-family: "Gelasio", Georgia, serif;
    font-size: 18px; color: var(--green);
  }
  .services__list li { display: flex; align-items: center; gap: 8px; white-space: nowrap; }
  .services__list li::before {
    content: ""; width: 11px; height: 11px; border-radius: 50%; background: var(--green); flex: none;
  }
  .services__licence {
    position: absolute; left: 140px; right: 0; top: 306px; text-align: center;
    font-family: "Tinos", "Times New Roman", serif;
    font-weight: 700; font-size: 15px; color: var(--ink-dark);
  }
</style>
</head>
<body>

<section class="card card--contact">
  <div class="contact__edge"></div>
  <div class="contact__corner"></div>
  <div class="contact__band"></div>
  <div class="contact__tab"></div>
  <div class="brand contact__brand"><span class="brand__dot"></span>TALLOWIND JOINERY WORKS</div>
  <h1 class="contact__name">Dorian Calvestri</h1>
  <div class="contact__details">
    <p>47 Quarrington Avenue, Hallsbury S.A 5099</p>
    <p><span>M: 0400 518 362</span><span>P: (08) 7010 4425</span><span>F: (08) 7010 4426</span></p>
    <p>dorian@tallowindjoinery.com.au</p>
  </div>
</section>

<section class="card card--services">
  <svg class="services__shapes" width="620" height="355" viewBox="0 0 620 355">
    <polygon points="0,150 140,68 140,355 0,355" fill="var(--grey)"/>
    <polygon points="0,150 140,68 140,82 0,165" fill="var(--black)"/>
    <polygon points="0,0 290,0 0,150" fill="var(--green-soft)"/>
  </svg>
  <div class="brand services__brand"><span class="brand__dot"></span>TALLOWIND JOINERY WORKS</div>
  <h2 class="services__title">Custom made</h2>
  <ul class="services__list">
    <li>Kitchens</li>
    <li>Laundry</li>
    <li>Entertainment units</li>
    <li>Vanities</li>
    <li>Robes</li>
    <li>Flat packs</li>
  </ul>
  <p class="services__licence">Lic. No. Bld 582904 Bld 740251</p>
</section>

</body>
</html>
```